FotoVELD buisnesscard

Hey :) I need a modern buisnesscard for my company FotoVELD
It most have:
Dagligleder og Fotograf: Eirik Tobias Vangsnes

Mob: +4791642508
Epost: post@fotoveld-eks.no
Adresse: Bjørkeveien22, 6099 Eksvik

Facbook and instagram logo with text FotoVELD

FotoVELD logo

It Company

```html
<!DOCTYPE html>
<html lang="no">
<head>
<meta charset="utf-8">
<title>FotoVELD – visittkort</title>
<link rel="stylesheet" href="https://fonts.googleapis.com/css2?family=Source+Sans+3:wght@400;700&display=swap">
<style>
  :root {
    --backdrop: #e4e5e7;
    --ink: #111111;
    --black: #0b0b0b;
    --grey-light: #cdcdcd;
    --grey-mid: #8c8c8c;
    --grey-dark: #707070;
    --white: #ffffff;
    --accent: #e8619d;
    --muted: #2a2a2a;
  }
  * { box-sizing: border-box; margin: 0; padding: 0; }
  html, body {
    width: 1200px; height: 876px; overflow: hidden;
    background: var(--backdrop);
    font-family: "Source Sans 3", "Myriad Pro", Arial, sans-serif;
  }
  .sheet {
    position: relative; width: 1200px; height: 876px;
    display: flex; align-items: center; justify-content: center; gap: 60px;
  }
  .card {
    position: relative; width: 520px; height: 336px; overflow: hidden;
    box-shadow: 0 6px 18px rgba(0,0,0,.18);
  }
  .card-shapes { position: absolute; inset: 0; }

  /* front */
  .front .brand-name {
    position: absolute; left: 34px; top: 42px;
    font-size: 40px; font-weight: 700; color: var(--white); letter-spacing: .5px;
  }
  .front .holder {
    position: absolute; right: 24px; top: 172px; text-align: right; color: var(--ink);
  }
  .holder-name { font-size: 22px; font-weight: 700; line-height: 1.15; }
  .holder-role { font-size: 17px; font-weight: 400; line-height: 1.2; }
  .front .contact {
    position: absolute; right: 24px; top: 254px; text-align: right;
    color: var(--white); font-size: 16px; line-height: 1.45;
  }

  /* back */
  .back { background: var(--grey-dark); }
  .back .brand-name {
    position: absolute; left: 0; right: 0; top: 150px; text-align: center;
    font-size: 46px; font-weight: 700; color: var(--accent); letter-spacing: .5px;
  }
  .social {
    position: absolute; display: flex; flex-direction: column; align-items: center; gap: 4px;
    color: var(--muted); font-size: 15px;
  }
  .social-mark { width: 14px; height: 14px; background: var(--muted); border-radius: 2px; }
  .social-left { left: 22px; top: 226px; }
  .social-right { right: 22px; top: 282px; }
</style>
</head>
<body>
<main class="sheet">

  <section class="card front" aria-label="Visittkort, forside">
    <svg class="card-shapes" viewBox="0 0 520 336" width="520" height="336" aria-hidden="true">
      <rect width="520" height="336" fill="var(--grey-mid)"/>
      <rect width="520" height="128" fill="var(--grey-light)"/>
      <polygon points="0,212 78,150 238,150 216,242 520,242 520,336 0,336" fill="var(--black)"/>
      <polyline points="0,206 76,144 236,144" fill="none" stroke="var(--white)" stroke-width="2"/>
      <polygon points="252,164 520,164 520,234 234,234" fill="var(--white)"/>
      <polygon points="238,164 246,164 228,234 220,234" fill="var(--white)"/>
    </svg>
    <div class="brand-name">FotoVELD</div>
    <div class="holder">
      <p class="holder-name">Eirik Tobias Vangsnes</p>
      <p class="holder-role">Dagligleder og Fotograf</p>
    </div>
    <div class="contact">
      <p>P: +4791642508</p>
      <p>E: post@fotoveld-eks.no</p>
      <p>Bjørkeveien22, 6099 Eksvik, Norway</p>
    </div>
  </section>

  <section class="card back" aria-label="Visittkort, bakside">
    <svg class="card-shapes" viewBox="0 0 520 336" width="520" height="336" aria-hidden="true">
      <rect width="520" height="336" fill="var(--grey-dark)"/>
      <rect width="520" height="140" fill="var(--black)"/>
    </svg>
    <div class="brand-name">FotoVELD</div>
    <div class="social social-left"><span class="social-mark"></span><span>FotoVELD</span></div>
    <div class="social social-right"><span class="social-mark"></span><span>FotoVELD</span></div>
  </section>

</main>
</body>
</html>
```